Electrical Contractor needs new Flyer

Update: need this flyer asap due to the flyer drop deadline coming soon.
Job Intro:
Design a DL Colour Flyer for a small Electrical Contracting company in the Eastern Suburbs of Melbourne VIC.
Specs:
Size: 99mmx210mm DL.
Paper to be printed on: 150gsm Glossy Paper.
PSD/PDF file must include bleed/crop marks.
Type: Double Sided
Colour: Front and Rear to be FULL colour.
Note: Thanks for the black and white flyers so far, but i think due to the fact iam paying for colour printing anyway, i will go only with colour. (unless you can show me otherwise that black and white can stand out better than colour)
Aim: To Target Local Customers in the area with a flyer that grabs there attention and makes them want to read more, instead of throwing out the flyer.
(there is allready other people putting out flyers in area)
Front Page Includes:
Company name: Calder Brook Electrical
REC: 48736 (can be small txt in a corner on front side, is legaly required to be displayed)
Phone: 1300 574 628
website: www.cbsparkworks.com.au
not required but happy to include:
Facebook Logo
www.facebook.com/cbsparkworks
include visa/mastercard pics
Rear of flyer:
to include work we do etc
We do not have a logo yet for our company, please feel free to design something to suite (keep in mind copyright etc)
you may read our website for info on what we do, but please dont use pictures of jobs etc from our work page. and try not just copy paste text into the flyer. (i can do that myself thats why im getting a designer to add the wow factor to it.
Looking for a Fresh modern looking flyer that will really get the readers attention.
(please no cheap looking cartons pics, also would like australian based looking cables, products if you are using pictures)
any more info please ask me thanks
I have included pics for ref, (such as my current cards and ute signage) please use as examples but dont just base the design on those thanks.
Also inc was my old flyers, i made them ,but they dont fit into the new DL flyer size so need to be re-sized etc.
Note: we may edit or change the winning design in future and this flyer will be copyright to us.

```html
<!DOCTYPE html>
<html lang="en">
<head>
<meta charset="utf-8">
<title>Calder Brook Electrical – Services Flyer</title>
<link rel="stylesheet" href="https://fonts.googleapis.com/css2?family=Fira+Sans:wght@400;500;600;700&display=swap">
<style>
  :root {
    --page: #ffffff;
    --frame: #8a8a8a;
    --ribbon: #fbf7d9;
    --ribbon-shadow: rgba(40, 30, 20, 0.5);
    --ink: #1e1e1e;
    --panel: rgba(250, 246, 232, 0.8);
    --offer: #f8c400;
    --offer-ink: #3b2a0c;
    --footer: #f3ab90;
    --footer-ink: #2f2f2f;
  }
  * { box-sizing: border-box; margin: 0; padding: 0; }
  html, body { width: 1200px; height: 626px; overflow: hidden; background: var(--page); }
  body { font-family: "Fira Sans", Arial, sans-serif; color: var(--ink); }

  .canvas {
    position: relative; width: 1200px; height: 626px;
    border: 1px solid var(--frame); background: var(--page);
  }
  .flyer {
    position: absolute; left: 53px; top: 55px; width: 1094px; height: 516px;
    overflow: hidden;
  }
  .light-rays {
    position: absolute; inset: 0;
    background:
      linear-gradient(180deg, #b88a5e 0%, rgba(184,138,94,0) 14%),
      linear-gradient(90deg, #c89a6c 0%, #e4cdb0 8%, #d9b08a 30%, #e6c7a5 50%, #d8d6b0 65%, #9fcfb0 82%, #b5d49c 100%);
  }
  .skyline {
    position: absolute; left: 0; right: 0; top: 290px; bottom: 0;
    background:
      linear-gradient(180deg, rgba(0,0,0,0) 0%, rgba(0,0,0,0) 20%, rgba(20,20,10,0.55) 55%, #141309 100%),
      linear-gradient(90deg, #5a5220 0%, #8a7a2a 12%, #c9c04a 24%, #6f7a30 38%, #9aa24a 52%, #c8cf6a 62%, #4f6a3a 74%, #7ea060 86%, #3e5a38 100%);
  }
  .bulb-scene {
    position: absolute; left: 85px; top: 0; width: 380px; height: 345px;
    background: radial-gradient(ellipse at 55% 10%, #efece4 0%, #c9c2b6 35%, #7d7162 75%, #4e443a 100%);
  }

  .ribbon {
    position: absolute; left: 75px; width: 395px; height: 40px;
    background: var(--ribbon);
    transform: rotate(-10deg); transform-origin: left center;
    box-shadow: 0 7px 6px var(--ribbon-shadow);
    font-size: 22px; font-weight: 500; line-height: 40px;
    padding-left: 30px; white-space: nowrap;
  }
  .ribbon--1 { top: 114px; }
  .ribbon--2 { top: 160px; }
  .ribbon--3 { top: 206px; }
  .ribbon--4 { top: 252px; }
  .ribbon--5 { top: 298px; }

  .services {
    position: absolute; left: 465px; top: 45px; width: 327px; height: 245px;
    background: var(--panel); list-style: none; padding: 9px 0 0 47px;
    font-size: 21px; line-height: 33.6px;
  }
  .services li { position: relative; }
  .services li::before {
    content: ""; position: absolute; left: -16px; top: 15px;
    width: 6px; height: 6px; border-radius: 50%; background: var(--ink);
  }

  .offer {
    position: absolute; left: 810px; top: 50px; width: 250px; height: 250px;
    border-radius: 50%; background: var(--offer); color: var(--offer-ink);
  }
  .offer__text {
    position: absolute; left: 16px; top: 46px; width: 222px;
    transform: rotate(-12deg); text-align: center; font-weight: 600;
  }
  .offer__title { font-size: 22px; }
  .offer__amount { font-size: 34px; font-weight: 700; line-height: 1.05; }
  .offer__terms { font-size: 16px; line-height: 1.2; }

  .credentials {
    position: absolute; left: 484px; top: 442px; width: 610px; height: 74px;
    background: var(--footer); color: var(--footer-ink);
    font-size: 19px; line-height: 74px; padding-left: 18px; white-space: nowrap;
  }
</style>
</head>
<body>
<div class="canvas">
  <section class="flyer">
    <div class="light-rays" role="img" aria-label="Warm streaks of coloured light"></div>
    <div class="skyline" role="img" aria-label="City skyline in yellow and green tones at dusk"></div>
    <div class="bulb-scene" role="img" aria-label="Glowing incandescent light bulb hanging in a dim room"></div>

    <div class="ribbon ribbon--1">Local Business (Based in Lilydale)</div>
    <div class="ribbon ribbon--2">Family Owned and Operated</div>
    <div class="ribbon ribbon--3">Competive Prices/Free Quotes</div>
    <div class="ribbon ribbon--4">No Job to Big or to Small</div>
    <div class="ribbon ribbon--5">Domestic and Commercial</div>

    <ul class="services">
      <li>Switchboard Upgrades</li>
      <li>Powerpoints and Lighting</li>
      <li>Solar Design and install</li>
      <li>Split Systems A/Cs</li>
      <li>New Homes or Renos</li>
      <li>Undergound Power</li>
      <li>Hot Water or Oven repairs</li>
    </ul>

    <div class="offer">
      <div class="offer__text">
        <p class="offer__title">Special Offer</p>
        <p class="offer__amount">$40 Discount</p>
        <p class="offer__terms">if you present this Flyer<br>Offer Ends 01/01/14 Ix<br>Per Customer Min<br>2hrs Labour required.</p>
      </div>
    </div>

    <div class="credentials">ABN: 41 982 607 315&nbsp; Solar Accreditation: A7304926 REC: 48736</div>
  </section>
</div>
</body>
</html>
```